We are looking for an effective ad to recruit work from home Loan Officers for our Mortgage Brokerage.
Use the following text...
Earn Mortgage Income in your sleep. Its as easy as 1, 2, 3.....
1) Solicit Potential Applicants (Word of Mouth, Email, Social Media etc.)
2) Take Complete Applications & Submit Them
3) Wait to Get Paid.......(Avg. $2,500 per closing)
"You open the door, we'll finish the deal"
No Experience Necessary
No Goals or Quotas
No Office Hours / Work from Home Office
...and We Fully Reimburse ALL LICENSING FEES!!
Email Resume to mwelby@brightharborloans.example
Bright Harbor Lending Group, Inc.
947 W Caldwell Avenue, #318
Baltimore, MD 21230
NMLS #731860
www.brightharborloans.example
Phone (800) 555-0142
Licensed Mortgage Broker in MD and DC since 1997
Target Market(s)
Professionals looking to earn part time income at Loan Officers, preferably with strong social media following.
Industry/Entity Type
Loan
Look and feel

```html
<!DOCTYPE html>
<html lang="en">
<head>
<meta charset="utf-8">
<title>Bright Harbor Lending Group – Loan Officer Recruitment</title>
<link rel="stylesheet" href="https://fonts.googleapis.com/css2?family=Arimo:wght@400;700&family=Roboto+Condensed:wght@700&family=EB+Garamond:ital@1&display=swap">
<style>
  :root {
    --page-bg: #e9e6e1;
    --paper: #ffffff;
    --brand-blue: #1f62ad;
    --headline-blue: #2765b0;
    --body-gray: #4a4a4a;
    --gold: #b59a3a;
    --photo-light: #f7efec;
    --photo-mid: #eed8d2;
    --photo-deep: #e3b9b6;
    --white: #ffffff;
  }
  * { margin: 0; padding: 0; box-sizing: border-box; }
  html, body { width: 1200px; height: 1000px; overflow: hidden; background: var(--page-bg); }
  .flyer {
    position: absolute; left: 284px; top: 50px; width: 696px; height: 900px;
    background: var(--paper); overflow: hidden;
    font-family: "Arimo", Arial, sans-serif;
  }
  .brand {
    position: absolute; left: 0; right: 0; top: 150px;
    display: flex; justify-content: center; align-items: center; gap: 12px;
  }
  .brand-dot { width: 26px; height: 26px; border-radius: 50%; background: var(--gold); }
  .brand-name { font-weight: 700; font-size: 26px; color: var(--brand-blue); }
  .headline {
    position: absolute; left: 0; right: 0; top: 248px; text-align: center;
    font-family: "Roboto Condensed", "Arial Narrow", sans-serif; font-weight: 700;
    font-size: 29px; color: var(--headline-blue);
  }
  .subhead {
    position: absolute; left: 0; right: 0; top: 286px; text-align: center;
    font-family: "EB Garamond", Georgia, serif; font-style: italic;
    font-size: 27px; color: var(--headline-blue);
  }
  .hero-photo {
    position: absolute; left: 305px; top: 372px; width: 391px; height: 420px;
    background: linear-gradient(180deg, var(--photo-light) 0%, var(--photo-mid) 60%, var(--photo-deep) 100%);
  }
  .steps {
    position: absolute; left: 46px; top: 336px; list-style: none;
    font-size: 10.5px; line-height: 13px; color: var(--body-gray);
  }
  .steps li { margin-bottom: 7px; }
  .steps .indent { padding-left: 10px; display: block; }
  .perks { position: absolute; left: 46px; top: 422px; color: var(--brand-blue); }
  .perks-quote {
    font-weight: 700; font-style: italic; font-size: 13.5px; line-height: 17px;
    letter-spacing: 0.3px; margin-bottom: 6px;
  }
  .perks ul { list-style: none; font-size: 11px; }
  .perks li { margin-bottom: 6px; }
  .perks .note { font-size: 10px; }
  .footer-band { position: absolute; left: 0; top: 725px; width: 696px; height: 175px; }
  .footer {
    position: absolute; left: 0; right: 0; top: 795px; text-align: center; color: var(--white);
  }
  .footer .email, .footer .web { font-weight: 700; font-size: 15px; line-height: 19px; }
  .footer .line { font-size: 12px; line-height: 17px; }
  .footer .tagline {
    margin-top: 6px; font-family: "EB Garamond", Georgia, serif; font-style: italic; font-size: 14px;
  }
  .social-badge {
    position: absolute; left: 609px; top: 860px; width: 62px; height: 22px;
    background: var(--white); border: 1px solid #c9d4e6;
  }
</style>
</head>
<body>
  <main class="flyer">
    <div class="brand">
      <span class="brand-dot"></span>
      <span class="brand-name">Bright Harbor Lending Group, Inc.</span>
    </div>

    <h1 class="headline">Earn Mortgage Income in your sleep.</h1>
    <p class="subhead">Its as easy as 1, 2, 3.....</p>

    <div class="hero-photo" role="img" aria-label="Photo of a smiling woman in a red top holding fanned dollar bills in both hands"></div>

    <ol class="steps">
      <li>1. Solicit Potential Applicants<span class="indent">(Word of Mouth, Email, Social Media etc.)</span></li>
      <li>2. Take Complete Applications &amp; Submit Them</li>
      <li>3. Wait to Get Paid.......(Avg. $2,500 per closing)</li>
    </ol>

    <div class="perks">
      <p class="perks-quote">“You open the door,<br>we’ll finish the deal”</p>
      <ul>
        <li>• No Experience Necessary</li>
        <li>• No Goals or Quotas</li>
        <li>• No Office Hours / Work from Home Office</li>
        <li class="note">...and We Fully Reimburse ALL LICENSING FEES!!</li>
      </ul>
    </div>

    <svg class="footer-band" viewBox="0 0 696 175" aria-hidden="true">
      <polygon points="0,3 350,60 696,5 696,175 0,175" fill="var(--brand-blue)"/>
    </svg>

    <div class="footer">
      <p class="email">Email Resume to mwelby@brightharborloans.example</p>
      <p class="line">Bright Harbor Lending Group, Inc.</p>
      <p class="line">947 W Caldwell Avenue, #318 • Baltimore, MD 21230 • NMLS #731860</p>
      <p class="web">www.brightharborloans.example • Phone (800) 555-0142</p>
      <p class="tagline">Licensed Mortgage Broker in MD and DC since 1997</p>
    </div>
    <div class="social-badge" aria-hidden="true"></div>
  </main>
</body>
</html>
```